Optometry practice sign/banner

Modern design appeal to mix demographic, family friendly. Emphasize the importance of eye exam.
Brigh colors, green,blue, yellow,
Photo of people wearing glasses
4'x8'

" EYE EXAM, CONTACT LENS, ORTHOK, LASIK CONSULTATION, DIABETES RETINAL EXAM
DR. NINA BOLT
BRIVAX OPTOMETRY " Eyecare for your family"
626.555.0183
MEDICAL, HELIXPLAN, QTR, ZORBEN, WALK IN WELCOME"

Target Market(s)

Family, middle age, mix demographic

Colors
33b8a4
fbee3d
cee9f5
9bcb3c

Requirements
Nice to have
• Photo of family wearing glasses.

```html
<!DOCTYPE html>
<html lang="en">
<head>
<meta charset="utf-8">
<title>Brivax Optometry Banner</title>
<link href="https://fonts.googleapis.com/css2?family=Arimo:wght@400;700&display=swap" rel="stylesheet">
<style>
  :root {
    --teal: #33b8a4;
    --yellow: #fbee3d;
    --sky: #cee9f5;
    --green: #9bcb3c;
    --ink: #111111;
    --panel: #fbfcf6;
    --panel-block: #f1f4e6;
    --stage: #e9eef2;
    --white: #ffffff;
    --wall: #eceae6;
    --shirt: #37a6dc;
    --denim: #3a4656;
  }
  * { box-sizing: border-box; margin: 0; padding: 0; }
  html, body {
    width: 1200px; height: 800px; overflow: hidden;
    background: var(--stage);
    font-family: "Arimo", Arial, sans-serif;
  }
  .banner {
    position: absolute; left: 40px; top: 120px;
    width: 1120px; height: 560px;
    overflow: hidden; background: var(--panel);
  }
  .family-photo {
    position: absolute; left: 0; top: 0; width: 800px; height: 560px;
    background:
      linear-gradient(180deg, rgba(0,0,0,0) 62%, var(--denim) 100%),
      linear-gradient(90deg, var(--wall) 0%, var(--wall) 18%, var(--shirt) 34%, var(--shirt) 80%, var(--wall) 100%);
  }
  .tagline-band {
    position: absolute; left: 0; top: 433px; width: 770px; height: 80px;
    background: rgba(51, 184, 164, .85);
    color: var(--white); font-weight: 700; font-size: 26px;
    padding: 24px 0 0 35px; white-space: nowrap;
  }
  .curves { position: absolute; inset: 0; }
  .coverage-tag {
    position: absolute; left: 31px; top: 20px; width: 320px; height: 73px;
    background: var(--green);
    clip-path: polygon(0 0, 100% 0, 83% 100%, 0 100%);
    color: var(--white); font-weight: 700; padding: 15px 0 0 18px;
  }
  .coverage-tag .plans { font-size: 12.5px; letter-spacing: .2px; }
  .coverage-tag .walk-in { font-size: 24px; margin-top: 4px; letter-spacing: .3px; }
  .brand {
    position: absolute; left: 930px; top: 20px; width: 150px;
    display: flex; flex-direction: column; align-items: center; gap: 10px;
  }
  .brand .mark { width: 98px; height: 116px; background: var(--yellow); }
  .brand .name {
    font-weight: 400; font-size: 15px; letter-spacing: 1.5px;
    color: var(--ink); text-align: center; line-height: 1.1;
  }
  .services {
    position: absolute; left: 873px; top: 224px; width: 218px;
    font-size: 17.5px; line-height: 23.5px; color: var(--ink);
  }
  .services span { display: block; white-space: nowrap; }
  .services .wide { letter-spacing: 3.4px; }
  .services .mid { letter-spacing: 1.4px; word-spacing: 8px; }
  .doctor {
    position: absolute; left: 864px; top: 390px;
    color: var(--green); font-weight: 700; font-size: 28px; letter-spacing: .5px;
  }
  .phone {
    position: absolute; left: 790px; top: 445px; width: 330px; height: 77px;
    text-align: right; padding: 17px 22px 0 0;
    font-weight: 700; font-size: 40px; color: var(--ink); letter-spacing: .5px;
  }
</style>
</head>
<body>
  <main class="banner">
    <div class="family-photo" role="img" aria-label="Smiling family of four in matching blue T-shirts and glasses, gathered around a laptop against a white brick wall"></div>

    <div class="tagline-band">BRIVAX OPTOMETRY " Eyecare for your family"</div>

    <svg class="curves" viewBox="0 0 1120 560" aria-hidden="true">
      <path d="M680,0 C790,120 810,360 690,560 L1120,560 L1120,0 Z" fill="var(--green)"/>
      <path d="M712,0 C815,120 830,360 712,560 L1120,560 L1120,0 Z" fill="var(--white)"/>
      <path d="M731,0 C840,120 850,360 728,560 L1120,560 L1120,0 Z" fill="var(--teal)"/>
      <path d="M773,0 C880,120 880,360 746,560 L1120,560 L1120,0 Z" fill="var(--panel)"/>
      <rect x="870" y="8" width="250" height="140" fill="var(--panel-block)"/>
      <rect x="860" y="205" width="260" height="150" fill="var(--panel-block)"/>
      <rect x="850" y="380" width="270" height="52" fill="var(--white)"/>
      <polygon points="800,445 1120,445 1120,522 760,522" fill="var(--yellow)"/>
    </svg>

    <div class="coverage-tag">
      <p class="plans">MEDICAL, HELIXPLAN, QTR, ZORBEN,</p>
      <p class="walk-in">WALK IN WELCOME</p>
    </div>

    <div class="brand">
      <span class="mark"></span>
      <span class="name">BRIVAX<br>OPTOMETRY</span>
    </div>

    <p class="services">
      <span class="mid">EYE EXAM, CONTACT</span>
      <span>LENS, ORTHOK, LASIK</span>
      <span class="wide">CONSULTATION,</span>
      <span class="mid">DIABETES RETINAL</span>
      <span>EXAM</span>
    </p>
    <p class="doctor">DR. NINA BOLT</p>
    <p class="phone">626.555.0183</p>
  </main>
</body>
</html>
```